Natural Cosmetics need a Packaging Design

We need a PACKAGING design for labels on hand/body wash bottles and soap paper boxes.
We target at high end markets.
We expect a contemporary and trendy design.
We don't need a separate logo. The brand name "Ma Vitrine" acts as the logo.
We want a modern and classic font for "Ma Vitrine".
Please see attached pictures for packaging samples.

Industry/Entity Type

Cosmetics

Requirements
Should not have
• a separate logo from the brand name

```html
<!DOCTYPE html>
<html lang="en">
<head>
<meta charset="utf-8">
<title>Ma Vitrine – Label Set</title>
<link rel="stylesheet" href="https://fonts.googleapis.com/css2?family=Quicksand:wght@400;500&family=Lora:wght@400&display=swap">
<style>
  :root {
    --coral: #ee5a5b;
    --coral-light: #f48d8a;
    --teal: #2aa4a1;
    --teal-light: #6ecbc6;
    --ink: #ffffff;
    --frame: rgba(255, 255, 255, 0.85);
    --page: #ffffff;
  }
  * { box-sizing: border-box; margin: 0; padding: 0; }
  html, body {
    width: 1172px; height: 1200px; overflow: hidden;
    background: var(--page);
  }
  .canvas { position: relative; width: 1172px; height: 1200px; }

  .label { position: absolute; overflow: hidden; }
  .label--coral { --base: var(--coral); --stripe: var(--coral-light); }
  .label--teal  { --base: var(--teal);  --stripe: var(--teal-light); }

  .label__pattern {
    position: absolute; inset: 0;
    background: linear-gradient(90deg, var(--base) 0%, var(--stripe) 50%, var(--base) 100%);
    opacity: 0.95;
  }

  .label__panel {
    position: absolute;
    background: var(--base);
    border: 1.5px solid var(--frame);
    outline: 1px solid var(--frame);
    outline-offset: -6px;
    display: flex; flex-direction: column; align-items: center; justify-content: center;
    color: var(--ink); text-align: center;
  }
  .label__brand {
    font-family: "Quicksand", sans-serif; font-weight: 500;
    line-height: 1;
  }
  .label__rule {
    width: 72%; height: 1px; background: var(--frame);
  }
  .label__product {
    font-family: "Quicksand", sans-serif; font-weight: 500;
    letter-spacing: 0.08em; line-height: 1;
  }
  .label__size {
    font-family: "Lora", serif; line-height: 1;
  }

  /* body wash labels */
  .label--body { top: 565px; width: 234px; height: 361px; }
  .label--body.label--coral { left: 127px; }
  .label--body.label--teal  { left: 451px; }
  .label--body .label__panel { left: 32px; top: 118px; width: 170px; height: 126px; }
  .label--body .label__brand { font-size: 28px; }
  .label--body .label__rule { margin: 10px 0 8px; }
  .label--body .label__product { font-size: 19px; }
  .label--body .label__size { font-size: 14px; margin-top: 12px; }

  /* soap wrap */
  .label--soap { left: 764px; top: 197px; width: 298px; height: 312px; }
  .label--soap .label__panel { left: 30px; top: 82px; width: 237px; height: 140px; }
  .label--soap .label__brand { font-size: 31px; }
  .label--soap .label__rule { margin: 12px 0 10px; }
  .label--soap .label__product { font-size: 21px; }
  .label--soap .label__size { font-size: 14px; margin-top: 12px; }

  /* hand wash label */
  .label--hand { left: 799px; top: 888px; width: 223px; height: 167px; }
  .label--hand .label__panel { left: 24px; top: 36px; width: 176px; height: 96px; }
  .label--hand .label__brand { font-size: 21px; }
  .label--hand .label__rule { margin: 7px 0 6px; }
  .label--hand .label__product { font-size: 15px; }
  .label--hand .label__size { font-size: 11px; margin-top: 8px; }
</style>
</head>
<body>
<main class="canvas">

  <section class="label label--body label--coral">
    <div class="label__pattern" role="img" aria-label="Wavy vertical stripe pattern in coral tones"></div>
    <div class="label__panel">
      <h1 class="label__brand">Ma Vitrine</h1>
      <span class="label__rule"></span>
      <p class="label__product">body wash</p>
      <p class="label__size">250ml</p>
    </div>
  </section>

  <section class="label label--body label--teal">
    <div class="label__pattern" role="img" aria-label="Wavy vertical stripe pattern in teal tones"></div>
    <div class="label__panel">
      <h2 class="label__brand">Ma Vitrine</h2>
      <span class="label__rule"></span>
      <p class="label__product">body wash</p>
      <p class="label__size">250ml</p>
    </div>
  </section>

  <section class="label label--soap label--coral">
    <div class="label__pattern" role="img" aria-label="Wavy vertical stripe pattern in coral tones"></div>
    <div class="label__panel">
      <h2 class="label__brand">Ma Vitrine</h2>
      <span class="label__rule"></span>
      <p class="label__product">beauty soap</p>
      <p class="label__size">100g</p>
    </div>
  </section>

  <section class="label label--hand label--coral">
    <div class="label__pattern" role="img" aria-label="Wavy vertical stripe pattern in coral tones"></div>
    <div class="label__panel">
      <h2 class="label__brand">Ma Vitrine</h2>
      <span class="label__rule"></span>
      <p class="label__product">hand wash</p>
      <p class="label__size">100ml</p>
    </div>
  </section>

</main>
</body>
</html>
```